Business Management System Providor Needs Upscale Business Card Design

We provide an online Claims Management System to the Insurance Industry called Meridell Casework Suite. Although our core offering is claims management, our system provides full business management features including reporting, invoicing, business trend analysis, etc..
We have a worldwide client base and our system has become known for its reliability, rich feature set, and intuitive design. This being the case we would like our cards to maintain a high level of professionalism. We have a tendency to lean toward a corporate look and feel and we would like to maintain that image.
Current Site: www.meridellcaseworksuite.example
Target Market(s)
Big Business, Insurance Professionals, Corporate Organizations
Industry/Entity Type
Business Management
Look and feel
Each slider illustrates characteristics of the customer's brand and the style your logo design should communicate.

```html
<!DOCTYPE html>
<html lang="en">
<head>
<meta charset="utf-8">
<title>Meridell Casework Suite – Business Cards</title>
<link href="https://fonts.googleapis.com/css2?family=Open+Sans:wght@400;600;700&family=Oswald:wght@400;500&display=swap" rel="stylesheet">
<style>
  :root {
    --page-bg: #e9e7e3;
    --card-white: #ffffff;
    --grey-band-light: #d6d7d9;
    --grey-band-dark: #a9abae;
    --brand-blue: #2f5286;
    --brand-blue-light: #4b6e9f;
    --brand-navy: #1f3a66;
    --text-dark: #3a3d42;
    --text-mid: #6b6f75;
    --map-tone: #e4e6ea;
  }
  * { box-sizing: border-box; margin: 0; padding: 0; }
  html, body {
    width: 1200px; height: 970px; overflow: hidden;
    background: var(--page-bg);
    font-family: "Open Sans", Arial, sans-serif;
  }
  .canvas {
    width: 1200px; height: 970px;
    display: flex; flex-direction: column; align-items: center; justify-content: center;
    gap: 30px;
  }
  .card {
    position: relative;
    width: 780px; height: 446px;
    background: var(--card-white);
    overflow: hidden;
    box-shadow: 0 6px 18px rgba(0,0,0,0.18);
  }
  /* ---------- brand lockup ---------- */
  .brand {
    position: absolute;
    display: flex; align-items: center; gap: 14px;
  }
  .brand-square {
    width: 44px; height: 44px; background: var(--brand-navy); flex: none;
  }
  .brand-name {
    font-weight: 700; font-size: 27px; color: var(--brand-navy); line-height: 1.05;
    white-space: nowrap;
  }
  .brand-tagline {
    font-size: 15px; color: var(--text-mid); letter-spacing: 0.3px; margin-top: 2px;
  }
  /* ---------- front card ---------- */
  .card-front .grey-band {
    position: absolute; left: 0; right: 0; top: 230px; height: 150px;
    background: linear-gradient(180deg, var(--grey-band-light), var(--grey-band-dark));
  }
  .card-front .band-notch { position: absolute; left: 160px; top: 230px; }
  .card-front .brand { left: 110px; top: 130px; }
  .card-front .website {
    position: absolute; left: 0; right: 0; top: 292px; text-align: center;
    font-size: 19px; letter-spacing: 6px; color: var(--text-dark);
  }
  /* ---------- back card ---------- */
  .card-back .world-map {
    position: absolute; left: 160px; top: 0; width: 620px; height: 260px;
    background: radial-gradient(ellipse at 55% 45%, var(--map-tone), var(--card-white) 70%);
  }
  .card-back .blue-band {
    position: absolute; left: 0; right: 0; top: 250px; bottom: 0;
    background: linear-gradient(90deg, var(--brand-blue-light), var(--brand-blue) 55%, var(--brand-navy));
  }
  .card-back .band-notch { position: absolute; left: 150px; top: 250px; }
  .card-back .brand { left: 90px; top: 100px; }
  .person {
    position: absolute; left: 60px; bottom: 34px; color: var(--card-white);
  }
  .person-name {
    font-family: "Oswald", "Arial Narrow", sans-serif;
    font-size: 40px; font-weight: 500; letter-spacing: 1px; line-height: 1;
    white-space: nowrap;
  }
  .person-role {
    font-size: 13px; letter-spacing: 2px; margin-top: 8px; text-transform: uppercase;
  }
  .contacts {
    position: absolute; right: 28px; top: 274px;
    display: grid; grid-template-columns: auto auto; column-gap: 26px; row-gap: 12px;
    color: var(--card-white); font-size: 12.5px;
  }
  .contact { display: flex; align-items: center; gap: 9px; white-space: nowrap; }
  .contact-wide { grid-column: 1 / span 2; }
  .contact svg { width: 20px; height: 20px; flex: none; }
</style>
</head>
<body>
<main class="canvas">

  <section class="card card-front" aria-label="Card front">
    <div class="grey-band"></div>
    <svg class="band-notch" width="36" height="18" viewBox="0 0 36 18" aria-hidden="true">
      <polygon points="0,0 36,0 18,18" fill="#ffffff"/>
    </svg>
    <div class="brand">
      <div class="brand-square"></div>
      <div>
        <div class="brand-name">Meridell Casework Suite</div>
        <div class="brand-tagline">claim management systems</div>
      </div>
    </div>
    <p class="website">www.meridellcaseworksuite.example</p>
  </section>

  <section class="card card-back" aria-label="Card back">
    <div class="world-map" role="img" aria-label="Faint world map in light grey"></div>
    <div class="blue-band"></div>
    <svg class="band-notch" width="36" height="18" viewBox="0 0 36 18" aria-hidden="true">
      <polygon points="0,0 36,0 18,18" fill="#ffffff"/>
    </svg>
    <div class="brand">
      <div class="brand-square"></div>
      <div>
        <div class="brand-name">Meridell Casework Suite</div>
        <div class="brand-tagline">claim management systems</div>
      </div>
    </div>

    <div class="person">
      <div class="person-name">DANA WHITLOW</div>
      <div class="person-role">General Manager</div>
    </div>

    <div class="contacts">
      <div class="contact">
        <svg viewBox="0 0 20 20" aria-hidden="true"><circle cx="10" cy="10" r="9" fill="none" stroke="#fff" stroke-width="1.3"/><path d="M7 5.5l2 2-1 1.2c.6 1.4 1.5 2.3 2.9 2.9l1.2-1 2 2-1.3 1.4c-3.3-.4-6.3-3.4-6.7-6.7z" fill="#fff"/></svg>
        <span>015 550 2841</span>
      </div>
      <div class="contact">
        <svg viewBox="0 0 20 20" aria-hidden="true"><circle cx="10" cy="10" r="9" fill="none" stroke="#fff" stroke-width="1.3"/><rect x="5.5" y="6.5" width="9" height="7" fill="none" stroke="#fff" stroke-width="1.2"/><path d="M5.5 6.5l4.5 4 4.5-4" fill="none" stroke="#fff" stroke-width="1.2"/></svg>
        <span>dana@meridell.example</span>
      </div>
      <div class="contact">
        <svg viewBox="0 0 20 20" aria-hidden="true"><circle cx="10" cy="10" r="9" fill="none" stroke="#fff" stroke-width="1.3"/><rect x="6" y="6" width="8" height="8" fill="none" stroke="#fff" stroke-width="1.2"/><path d="M8 14v2h4v-2" fill="none" stroke="#fff" stroke-width="1.2"/></svg>
        <span>015 550 2842</span>
      </div>
      <div class="contact">
        <svg viewBox="0 0 20 20" aria-hidden="true"><circle cx="10" cy="10" r="9" fill="none" stroke="#fff" stroke-width="1.3"/><circle cx="10" cy="10" r="4.5" fill="none" stroke="#fff" stroke-width="1.2"/><path d="M5.5 10h9M10 5.5v9" stroke="#fff" stroke-width="1"/></svg>
        <span>www.meridellcaseworksuite.example</span>
      </div>
      <div class="contact contact-wide">
        <svg viewBox="0 0 20 20" aria-hidden="true"><circle cx="10" cy="10" r="9" fill="none" stroke="#fff" stroke-width="1.3"/><path d="M10 15s-3.5-4-3.5-6.3a3.5 3.5 0 0 1 7 0C13.5 11 10 15 10 15z" fill="#fff"/><circle cx="10" cy="8.7" r="1.2" fill="#2f5286"/></svg>
        <span>42 Harbor Lane, Suite 3, Westgate</span>
      </div>
    </div>
  </section>

</main>
</body>
</html>
```